Corporate Cover & Profile Images - YouTube, Google+, Facebook, Instagram, Twitter, Linkedin, Pint...

I need corporate social media cover & profile images created for YouTube, Google+, Facebook, Instagram, Twitter, Linkedin, and Pintrest. Our logo, an image of our doctors, and fonts are attached. Website URL is quenbrookclinic.com. Design must match our overall branding and color scheme. I also need our phone number of 877-555-0163 prominently displayed in the cover images. If you want to incorporate results images they can be found here: https://quenbrookclinic.com/results/hair-transplant-before-and-after/ If stock images are used please provide the URL so I can purchase the proper usage license. Must deliver original photoshop PSD files and final images sized correctly for each social account.

```html
<!DOCTYPE html>
<html lang="en">
<head>
<meta charset="utf-8">
<title>Quenbrook Clinic – Social Cover Set</title>
<link rel="stylesheet" href="https://fonts.googleapis.com/css2?family=Montserrat:wght@500;600&display=swap">
<style>
  :root {
    --board: #e4e4e4;
    --paper: #ffffff;
    --teal-deep: #0d6a73;
    --teal-soft: #a4c9c4;
    --teal-ink: #13646d;
    --brand-brown: #5d5048;
    --scrub-navy: #1f3568;
  }
  * { margin: 0; padding: 0; box-sizing: border-box; }
  html, body { width: 1200px; height: 1200px; overflow: hidden; }
  body {
    background: var(--board);
    font-family: "Montserrat", sans-serif;
    position: relative;
  }
  .cover {
    position: absolute;
    left: 70px;
    width: 1068px;
    background: var(--paper);
    overflow: hidden;
    box-shadow: 2px 3px 4px rgba(0,0,0,0.35);
  }
  .cover--wide { top: 109px; height: 395px; }
  .cover--tall { top: 534px; height: 598px; }
  .band, .team-photo, .text, .rule { position: absolute; }
  .band--soft { background: var(--teal-soft); }
  .band--deep { background: linear-gradient(180deg, #0f6f78, #0a5e6b); }
  .team-photo {
    z-index: 1;
    background: linear-gradient(180deg, #f4f1ee 0%, #e8c7b4 28%, var(--scrub-navy) 55%, #1a2d5c 100%);
  }
  .text {
    z-index: 2;
    white-space: nowrap;
    text-transform: uppercase;
    font-weight: 600;
  }
  .text--center { text-align: center; }
  .text--right { text-align: right; }
  .text--left { text-align: left; }
  .rule { z-index: 2; height: 2px; background: #ffffff; }
  .brand-name { color: var(--brand-brown); letter-spacing: 0.02em; }
  .tagline { color: var(--teal-ink); letter-spacing: 0.14em; }
  .claim { color: var(--teal-ink); letter-spacing: 0.14em; line-height: 1; }
  .on-deep { color: #ffffff; letter-spacing: 0.14em; font-weight: 500; line-height: 1; }
  .web { color: var(--teal-ink); letter-spacing: 0.16em; }
</style>
</head>
<body>

  <section class="cover cover--wide">
    <div class="text text--center brand-name" style="left:394px; width:674px; top:94px; font-size:44px;">Quenbrook Clinic</div>

    <div class="band band--soft" style="left:394px; top:160px; width:674px; height:38px;"></div>
    <div class="text text--center tagline" style="left:394px; width:674px; top:169px; font-size:18px;">Hair Transplant &amp; Hair Restoration</div>

    <div class="text text--center claim" style="left:394px; width:674px; top:214px; font-size:24px;">Best Hair</div>
    <div class="text text--center claim" style="left:394px; width:674px; top:238px; font-size:30px;">Doctors</div>

    <div class="band band--deep" style="left:474px; top:274px; width:594px; height:76px;"></div>
    <div class="text text--center on-deep" style="left:394px; width:674px; top:285px; font-size:25px;">Call Now</div>
    <div class="text text--center on-deep" style="left:394px; width:674px; top:312px; font-size:31px; font-weight:600;">877-555-0163</div>

    <div class="band band--soft" style="left:454px; top:350px; width:614px; height:45px;"></div>
    <div class="text text--center web" style="left:394px; width:674px; top:362px; font-size:18px;">quenbrookclinic.com</div>

    <div class="team-photo" role="img" aria-label="Photo of the four clinic doctors in navy scrubs, arms crossed, smiling" style="left:0; top:27px; width:480px; height:368px;"></div>
  </section>

  <section class="cover cover--tall">
    <div class="text text--center brand-name" style="left:0; width:1068px; top:124px; font-size:50px;">Quenbrook Clinic</div>

    <div class="band band--soft" style="left:0; top:222px; width:1068px; height:43px;"></div>
    <div class="text text--center tagline" style="left:0; width:1068px; top:230px; font-size:25px;">Hair Transplant &amp; Hair Restoration</div>

    <div class="band band--deep" style="left:0; top:392px; width:1068px; height:141px;"></div>

    <div class="rule" style="left:0; top:426px; width:134px;"></div>
    <div class="text text--right on-deep" style="left:60px; width:218px; top:418px; font-size:19px;">Best Hair</div>
    <div class="text text--right on-deep" style="left:40px; width:222px; top:446px; font-size:25px;">Doctors</div>

    <div class="text text--left on-deep" style="left:783px; width:150px; top:420px; font-size:19px;">Call Now</div>
    <div class="rule" style="left:934px; top:429px; width:134px;"></div>
    <div class="text text--left on-deep" style="left:812px; width:256px; top:446px; font-size:25px;">877-555-0163</div>

    <div class="team-photo" role="img" aria-label="Photo of the four clinic doctors in navy scrubs, smiling, shoulder to shoulder" style="left:290px; top:265px; width:480px; height:268px;"></div>

    <div class="band band--soft" style="left:0; top:533px; width:1068px; height:65px;"></div>
    <div class="text text--center web" style="left:0; width:1068px; top:548px; font-size:30px;">quenbrookclinic.com</div>
  </section>

</body>
</html>
```